Electrical contractor in San Diego county since 1988

Provide a company name/ logo for business cards and forms. Newer and more modern old card is attached. Color preference is black and orange. Simple and streamlined nothing too busy. I have also attached a card that represents the simplicity of what we are looking for.

Contractor

```html
<!DOCTYPE html>
<html lang="en">
<head>
<meta charset="utf-8">
<title>D.W. Current Inc. – Business Card</title>
<link rel="stylesheet" href="https://fonts.googleapis.com/css2?family=EB+Garamond:ital,wght@0,400;0,700;1,700&family=Open+Sans:wght@300;700&display=swap">
<style>
  :root {
    --ink: #111111;
    --paper: #ffffff;
    --frame: #9a9a9a;
    --orange-deep: #ee9a22;
    --orange-light: #fbe3c2;
  }
  html, body {
    margin: 0;
    padding: 0;
    width: 1200px;
    height: 686px;
    overflow: hidden;
    background: var(--paper);
  }
  .card {
    display: block;
    width: 1200px;
    height: 686px;
  }
  .card-frame { fill: var(--paper); stroke: var(--frame); stroke-width: 1.5; }
  .serif { font-family: "EB Garamond", Garamond, serif; fill: var(--ink); }
  .sans { font-family: "Open Sans", Arial, sans-serif; fill: var(--ink); }
  .tagline { font-size: 28px; }
  .company-name { font-size: 67px; font-weight: 700; letter-spacing: 1px; }
  .company-services { font-size: 42px; font-weight: 300; letter-spacing: 0.5px; }
  .person-line { font-size: 46px; font-weight: 700; font-variant: small-caps; }
  .person-title { font-style: italic; font-variant: normal; }
  .contact { font-size: 39px; }
</style>
</head>
<body>
<svg class="card" viewBox="0 0 1200 686" xmlns="http://www.w3.org/2000/svg">
  <defs>
    <linearGradient id="markGradient" x1="0" y1="0" x2="1" y2="1">
      <stop offset="0" stop-color="var(--orange-deep)"/>
      <stop offset="0.5" stop-color="var(--orange-light)"/>
      <stop offset="1" stop-color="var(--orange-deep)"/>
    </linearGradient>
  </defs>

  <rect class="card-frame" x="0.75" y="0.75" width="1198.5" height="684.5"/>

  <rect class="brand-mark-area" x="980" y="16" width="163" height="455" fill="url(#markGradient)"
        role="img" aria-label="Area for an orange lightning bolt brand mark"/>

  <text class="serif tagline" x="599" y="91" text-anchor="middle">Serving San Diego since 1988 - Lic. 714263</text>

  <text class="sans company-name" x="599" y="229" text-anchor="middle">D.W. Current Inc.</text>
  <text class="sans company-services" x="599" y="288" text-anchor="middle">Commercial - New &amp; Remodel</text>

  <text class="serif person-line" x="599" y="423" text-anchor="middle">Dennis Walsh - <tspan class="person-title">President</tspan></text>

  <text class="serif contact" x="88" y="551">P.O. Box 2718</text>
  <text class="serif contact" x="88" y="608">Cedar Ridge, CA 92099-0412</text>

  <text class="serif contact" x="1157" y="551" text-anchor="end">619.555.0147</text>
  <text class="serif contact" x="1157" y="608" text-anchor="end">Fax 619.555.0182</text>
</svg>
</body>
</html>
```